Harbourline Blinds & Shutters

It Needs to look classy as my target is the upper end of the blind market
I need a Logo design on front and description on back of what i do:
- Roller Blinds
- Vertical Blinds
- Venetian Blinds
- Plantation Shutters
- Aluminum External Shutters
and contact details
Declan
0418275063
and
Trent
0419852306
Updates
Hi Guys,
Sorry for the no feedback but i was waiting on my logo design. But its done now i have uploaded it. so if you could take a look and send through some designs
Reason: my logo was just finished an i just uploaded it today really dont understand why my deadline has been rached foe my bizcards as it states no deadline. But please extend
Target Market(s)
People that live on the coast and are looking for classy good quality blinds and shutters
Font styles to use
Other font styles liked:
- Copperplate Gothic,open to suggestion
Look and feel
Each slider illustrates characteristics of the customer's brand and the style your logo design should communicate.

```html
<!DOCTYPE html>
<html lang="en">
<head>
<meta charset="utf-8">
<title>Harbourline Blinds &amp; Shutters – Business Card</title>
<link href="https://fonts.googleapis.com/css2?family=Jost:wght@400;600&display=swap" rel="stylesheet">
<style>
  :root {
    --backdrop: #e4e4e4;
    --card-dark: #0b0b0b;
    --card-light: #ffffff;
    --ink-dark: #111111;
    --ink-light: #ffffff;
    --shadow: rgba(0, 0, 0, 0.25);
  }
  * { box-sizing: border-box; margin: 0; padding: 0; }
  html, body {
    width: 1200px;
    height: 720px;
    overflow: hidden;
    background: var(--backdrop);
    font-family: "Jost", "Century Gothic", sans-serif;
  }
  .card-set {
    position: absolute;
    top: 196px;
    left: 40px;
    display: flex;
    gap: 40px;
  }
  .card {
    width: 540px;
    height: 328px;
    box-shadow: 0 10px 28px var(--shadow);
    display: flex;
    flex-direction: column;
    align-items: center;
    justify-content: center;
    text-align: center;
  }
  .card--front {
    background: var(--card-dark);
    color: var(--ink-light);
  }
  .card--back {
    background: var(--card-light);
    color: var(--ink-dark);
    padding: 30px 40px;
    justify-content: space-between;
  }
  .brand-name {
    font-weight: 600;
    text-transform: uppercase;
    letter-spacing: 0.06em;
  }
  .card--front .brand-name {
    font-size: 30px;
    line-height: 1.25;
  }
  .card--back .brand-name {
    font-size: 24px;
  }
  .service-list {
    list-style: none;
    font-weight: 600;
    font-size: 17px;
    line-height: 1.45;
  }
  .contacts {
    display: flex;
    align-items: stretch;
    font-size: 15px;
  }
  .contact {
    padding: 0 16px;
    display: flex;
    flex-direction: column;
    gap: 2px;
  }
  .contact + .contact { border-left: 1.5px solid var(--ink-dark); }
  .contact-name { font-weight: 600; }
  .contact-phone {
    display: flex;
    align-items: center;
    gap: 5px;
    font-weight: 400;
  }
  .contact--left .contact-phone { flex-direction: row-reverse; }
  .phone-icon { width: 10px; height: 14px; }
</style>
</head>
<body>
  <main class="card-set">
    <section class="card card--front" aria-label="Card front">
      <h1 class="brand-name">Harbourline Blinds<br>&amp; Shutters</h1>
    </section>

    <section class="card card--back" aria-label="Card back">
      <h2 class="brand-name">Harbourline Blinds &amp; Shutters</h2>

      <ul class="service-list">
        <li>- Roller Blinds -</li>
        <li>- Vertical Blinds -</li>
        <li>- Venetian Blinds -</li>
        <li>- Plantation Shutters -</li>
        <li>- Aluminum External Shutters -</li>
      </ul>

      <div class="contacts">
        <div class="contact contact--left">
          <span class="contact-name">Declan</span>
          <span class="contact-phone">
            <svg class="phone-icon" viewBox="0 0 10 14" aria-hidden="true"><rect x="0.75" y="0.75" width="8.5" height="12.5" rx="1.5" fill="none" stroke="currentColor" stroke-width="1.5"/><rect x="2.5" y="2.5" width="5" height="6" fill="currentColor"/></svg>
            0418275063
          </span>
        </div>
        <div class="contact contact--right">
          <span class="contact-name">Trent</span>
          <span class="contact-phone">
            <svg class="phone-icon" viewBox="0 0 10 14" aria-hidden="true"><rect x="0.75" y="0.75" width="8.5" height="12.5" rx="1.5" fill="none" stroke="currentColor" stroke-width="1.5"/><rect x="2.5" y="2.5" width="5" height="6" fill="currentColor"/></svg>
            0419852306
          </span>
        </div>
      </div>
    </section>
  </main>
</body>
</html>
```